dessert restaurant

I need a business card design for my restaurant. It will primarily be a dessert and wine restaurant. I will serve delicious baked from scratch desserts, cake, pies cookies brownies etc. Select red and white wines.I will also offer light breakfast, and lunch menu. This will be an upscale contemporary design restaurant with reasonably priced items on the menu. I will also offer small plates in the evening with dessert menu. my color scheme is cobalt blue , red, white black. My restaurant will be the place where adults come after enjoying the meal at a restaurant and want to enjoy a dessert and a glass of wine to finish off their evening. I will also have contemporary jazz sounds for atmosphere.

Industry/Entity Type

Restaurant

Contact Information for Business Card

delia marsh 415 862 3094

```html
<!DOCTYPE html>
<html lang="en">
<head>
<meta charset="utf-8">
<title>Velvetine — Delia Marsh</title>
<link href="https://fonts.googleapis.com/css2?family=Cormorant+Garamond:ital,wght@0,400;0,500;1,400;1,500&display=swap" rel="stylesheet">
<style>
  :root {
    --teal-light: #2f93a8;
    --teal-mid: #15566d;
    --teal-deep: #0a2233;
    --ink: #0a0f14;
    --ink-soft: #1d2830;
    --silver: #c9ccd0;
    --silver-dim: #8d9399;
    --white: #ffffff;
    --rule: #a9b2b8;
  }
  html, body {
    margin: 0;
    padding: 0;
    overflow: hidden;
    background: #e6e6e6;
  }
  .card {
    position: relative;
    width: 1200px;
    height: 702px;
    overflow: hidden;
    background: var(--ink);
    font-family: "Cormorant Garamond", "Times New Roman", serif;
  }
  .card__header {
    position: absolute;
    left: 0; top: 0;
    width: 1200px; height: 318px;
    background:
      radial-gradient(ellipse 55% 60% at 52% 0%, var(--teal-light) 0%, rgba(47,147,168,0) 70%),
      linear-gradient(180deg, var(--teal-mid) 0%, #12445a 45%, var(--teal-deep) 100%);
  }
  .brand {
    position: absolute;
    left: 430px; top: 88px;
    display: flex;
    align-items: center;
    gap: 18px;
  }
  .brand__dot {
    width: 46px; height: 46px;
    border-radius: 50%;
    background: var(--white);
  }
  .brand__name {
    color: var(--white);
    font-style: italic;
    font-weight: 500;
    font-size: 42px;
    letter-spacing: 1px;
  }
  .person {
    position: absolute;
    left: 0; top: 194px;
    width: 1200px;
    text-align: center;
  }
  .person__name {
    display: inline-block;
    margin: 0;
    color: var(--silver);
    font-weight: 400;
    font-size: 52px;
    letter-spacing: 3px;
    line-height: 1;
    padding: 0 6px 8px;
    border-bottom: 1px solid var(--rule);
  }
  .person__tel {
    margin: 12px 0 0;
    color: var(--silver);
    font-size: 22px;
    letter-spacing: 1px;
  }
  .person__tel em { font-style: italic; }
  .strip-rule {
    position: absolute;
    left: 0; width: 1200px; height: 3px;
    background: linear-gradient(90deg, #555c62, #d8dcdf 50%, #555c62);
  }
  .strip-rule--top { top: 316px; }
  .strip-rule--bottom { top: 602px; }
  .gallery {
    position: absolute;
    left: 0; top: 319px;
    width: 1200px; height: 283px;
    display: flex;
    gap: 4px;
    background: #d8d8d8;
  }
  .gallery__photo { flex: 1; height: 100%; }
  .gallery__photo--waffles {
    background: radial-gradient(ellipse at 45% 60%, #d8a45a 0%, #9a5a25 50%, #3a2415 100%);
  }
  .gallery__photo--soup {
    background: radial-gradient(ellipse at 50% 55%, #e9dfb5 0%, #b8845a 40%, #4f6b3a 75%, #2a2a2a 100%);
  }
  .gallery__photo--desserts {
    background: linear-gradient(160deg, #2a1812 0%, #5a3524 55%, #c7b8a8 85%, #3a2418 100%);
  }
  .card__footer {
    position: absolute;
    left: 0; top: 605px;
    width: 1200px; height: 97px;
    background: linear-gradient(180deg, var(--ink-soft) 0%, var(--ink) 100%);
  }
  .address {
    position: absolute;
    left: 0; top: 18px;
    width: 1200px;
    margin: 0;
    text-align: center;
    color: var(--silver-dim);
    font-size: 20px;
    letter-spacing: 0.5px;
  }
</style>
</head>
<body>
  <div class="card">
    <header class="card__header" role="img" aria-label="Deep teal damask patterned background">
    </header>
    <div class="brand">
      <span class="brand__dot"></span>
      <span class="brand__name">Velvetine</span>
    </div>
    <div class="person">
      <h1 class="person__name">Delia Marsh</h1>
      <p class="person__tel"><em>Tel no.:</em> 415 862 3094</p>
    </div>
    <div class="strip-rule strip-rule--top"></div>
    <section class="gallery">
      <div class="gallery__photo gallery__photo--waffles" role="img" aria-label="Photo of fried chicken on a waffle"></div>
      <div class="gallery__photo gallery__photo--soup" role="img" aria-label="Photo of soup, sandwich and green salad"></div>
      <div class="gallery__photo gallery__photo--desserts" role="img" aria-label="Photo of cheesecake, cupcake, hot chocolate and red wine"></div>
    </section>
    <div class="strip-rule strip-rule--bottom"></div>
    <footer class="card__footer">
      <p class="address">1187 Larkspur Street, N.W., Washington, D.C. 20010</p>
    </footer>
  </div>
</body>
</html>
```